New Chartered Accounting Practice Needs Stationery Design

I need a new set of stationery including letterhead, business cards, envelopes and with compliments slips for a new Chartered Accounting Practice based in Melbourne, Victoria, Australia called "Martin K. Ashbury, Chartered Accountant".
I will be providing Taxation Services, Accounting Services, Self-Managed Superannuation Fund Consulting and general consulting advice to small and medium business enterprises. I would like to see designs that use the colour blue. The final design should communicate trust, technical expertise and security.
Target Market(s)
English speaking, Australians. Proprietors of small and medium businesses - aged 30-65. Fellow professionals - lawyers, investment consultants, other accountants. Retirees - aged 60 and over
Industry/Entity Type
Business
Look and feel

```html
<!DOCTYPE html>
<html lang="en">
<head>
<meta charset="utf-8">
<title>Martin K. Ashbury – Stationery</title>
<link href="https://fonts.googleapis.com/css2?family=Crimson+Text:wght@400;600&display=swap" rel="stylesheet">
<style>
  :root {
    --backdrop: #e4e5e7;
    --paper: #ffffff;
    --edge: #cfd3d8;
    --blue-deep: #0b4391;
    --blue-mid: #2a78c6;
    --ink-light: #ffffff;
    --ink-grey: #4a4f55;
  }
  * { margin: 0; padding: 0; box-sizing: border-box; }
  html, body {
    width: 1200px; height: 898px; overflow: hidden;
    background: var(--backdrop);
    font-family: "Crimson Text", Georgia, serif;
  }
  .sheet {
    position: absolute;
    background: var(--paper);
    border: 1px solid var(--edge);
    overflow: hidden;
  }
  .band { position: absolute; left: 0; right: 0; }
  .band-top { top: 0; background: linear-gradient(180deg, var(--blue-deep), var(--blue-mid)); }
  .band-foot { bottom: 0; background: linear-gradient(180deg, var(--blue-mid), var(--blue-deep)); }
  .brand { position: absolute; color: var(--ink-light); line-height: 1.1; }
  .brand-name { font-weight: 600; display: block; }
  .brand-role { font-weight: 400; display: block; }
  .contact { position: absolute; font-size: 10.5px; line-height: 1.25; }
  .contact p { white-space: nowrap; }
  .align-right { text-align: right; }

  /* Letterhead */
  .letterhead { left: 79px; top: 27px; width: 649px; height: 842px; }
  .letterhead .band-top { height: 96px; }
  .letterhead .band-foot { height: 74px; }
  .letterhead .brand { left: 19px; top: 22px; }
  .letterhead .brand-name { font-size: 19px; }
  .letterhead .brand-role { font-size: 13px; margin-top: 1px; }
  .letterhead .contact { color: var(--ink-light); }
  .letterhead .contact-personal { left: 19px; bottom: 8px; }
  .letterhead .contact-office { right: 19px; bottom: 8px; }

  /* Envelope */
  .envelope { left: 325px; top: 357px; width: 793px; height: 396px; }
  .envelope .band-foot { height: 86px; }
  .envelope .brand { left: 21px; top: 352px; }
  .envelope .brand-name { font-size: 16.5px; }
  .envelope .brand-role { font-size: 11.5px; margin-top: 1px; }
  .envelope .contact { color: var(--ink-light); right: 18px; bottom: 6px; font-size: 10.8px; }

  /* Business card */
  .business-card { left: 802px; top: 129px; width: 316px; height: 193px; }
  .business-card .band-top { height: 52px; }
  .business-card .brand { left: 8px; top: 8px; }
  .business-card .brand-name { font-size: 16px; }
  .business-card .brand-role { font-size: 11px; margin-top: 1px; }
  .business-card .contact { color: var(--ink-grey); font-size: 10.5px; }
  .business-card .contact-personal { left: 7px; bottom: 5px; }
  .business-card .contact-office { right: 6px; bottom: 5px; }
</style>
</head>
<body>

<section class="sheet letterhead" aria-label="Letterhead">
  <div class="band band-top" role="img" aria-label="Blue header band"></div>
  <div class="band band-foot" role="img" aria-label="Blue footer band"></div>
  <div class="brand">
    <span class="brand-name">Martin K. Ashbury</span>
    <span class="brand-role">Chartered Accountant</span>
  </div>
  <div class="contact contact-personal">
    <p>Mobile : +00-1234567890</p>
    <p>E-mail ID: office@ashburyca.net</p>
  </div>
  <div class="contact contact-office align-right">
    <p>Address Line1,</p>
    <p>Address Line2,</p>
    <p>Address Line3</p>
    <p>Telephone : 12345 67890 | TeleFax : +0-11-222 3333</p>
  </div>
</section>

<section class="sheet envelope" aria-label="Envelope">
  <div class="band band-foot" role="img" aria-label="Blue footer band"></div>
  <div class="brand">
    <span class="brand-name">Martin K. Ashbury</span>
    <span class="brand-role">Chartered Accountant</span>
  </div>
  <div class="contact align-right">
    <p>Address Line1,</p>
    <p>Address Line2,</p>
    <p>Address Line3.</p>
    <p>Telephone : 12345 67890 | TeleFax : +0-11-222 3333</p>
    <p>Mobile : +00-1234567890 | E-mail ID: office@ashburyca.net</p>
  </div>
</section>

<section class="sheet business-card" aria-label="Business card">
  <div class="band band-top" role="img" aria-label="Blue header band"></div>
  <div class="brand">
    <span class="brand-name">Martin K. Ashbury</span>
    <span class="brand-role">Chartered Accountant</span>
  </div>
  <div class="contact contact-personal">
    <p>Mobile : +00-12345 67890</p>
    <p>E-mail ID: office@ashburyca.net</p>
  </div>
  <div class="contact contact-office align-right">
    <p>Address Line1,</p>
    <p>Address Line2,</p>
    <p>Address Line3.</p>
    <p>Telephone : 12345 67890</p>
    <p>TeleFax : +0-11-222 3333</p>
  </div>
</section>

</body>
</html>
```